Purchasing Management Consulting B to B Web Design PAYMENT GUARANTY

We'd like to build a new digital image for our website.

Our company is managing purchasing consultancy services for Large and Medium companies around 4 activities :
- Procurement outsourcing
- Purchasing consulting (cost reduction)
- Supply chain training
- Web platform to manage Supplier risk (TrusoMark.com)

We now aim to harmonies our website in term of design in order to build a strongest Corporate Image.

SEE REQUIREMENT ENCLOSED

Please have a look on our current websites:
- www.procuvantix.com
- www.pqz-network.com
- www.trusomark.com

Reason: Hello, Some project received are not really professional and need more details. I did not see all deliverable requested in specifications. I'll revert to designer to improve design. Regards, Bastien

Reason: Only few designers reply and feedback still need to be done.

Target Market(s)

Our business is exclusively Business to Business toward Medium and Large companies.

Industry/Entity Type

Digital

Requirements
Must have
• Website will be developped in Joomla CMS.
The user community will use Fellowkit module : Visitor should be "influenced" to communicate its contact details by registering the community.

Ergonomy, Simplicity and professionnalism is the key objectives.

Deliverables :
- Corporate Home page including clear access to our 4 activities
- Dynamique banner
- Corporate article / contact pages (1 or 2)
- Activities home pages (x 4)
- Activity Catalog (Indesign for paper version)
Nice to have
• Integration of Design for our consulting and training catalog will be interesting.

Livechat design (the one of Craftplaza.com is good)
Should not have
• Only psd

Not html

```html
<!DOCTYPE html>
<html lang="fr">
<head>
<meta charset="utf-8">
<title>PVX – Procurement Consulting</title>
<link rel="stylesheet" href="https://fonts.googleapis.com/css2?family=Questrial&family=Arvo:wght@700&family=Yanone+Kaffeesatz:wght@400;500&display=swap">
<style>
  :root{
    --orange:#f6b20e;
    --orange-dark:#e79d05;
    --lime:#c9cf1a;
    --lime-dark:#a9b012;
    --ink:#3b3a4f;
    --text:#6b6b6b;
    --muted:#9a9a9a;
    --panel:#ececec;
    --footer:#57565f;
    --white:#ffffff;
  }
  *{box-sizing:border-box;margin:0;padding:0}
  html,body{width:1095px;height:1200px;overflow:hidden;background:var(--white)}
  body{position:relative;font-family:"Questrial",sans-serif;color:var(--text)}
  .abs{position:absolute}

  .hero-art{left:0;top:0;width:1095px;height:470px;
    background:radial-gradient(ellipse at 50% 60%,#ffffff 0%,#f1f1f1 45%,#d6d6d6 80%,#c9c9c9 100%)}

  .brand{left:122px;top:12px;width:170px;height:120px;display:flex;align-items:center;gap:8px}
  .brand-disc{width:96px;height:96px;border-radius:50%;background:var(--orange)}
  .brand-name{font-family:"Questrial",sans-serif;font-size:34px;color:var(--ink)}

  .login input{position:absolute;height:22px;border:1px solid #d7d7d7;background:#fafafa;
    font:10px "Questrial",sans-serif;color:#888;padding:0 6px}
  .login-btn{left:769px;top:19px;width:52px;height:22px;background:var(--orange);
    font:bold 10px "Questrial",sans-serif;color:#3b3a4f;display:flex;align-items:center;justify-content:center}

  .social{display:flex;gap:6px}
  .social span{width:25px;height:25px;border-radius:50%;background:#8f8f8f;display:block}

  .main-nav{left:291px;top:53px;width:684px;height:37px;background:var(--orange);border-radius:0 4px 4px 0;
    display:flex;align-items:center;padding-left:30px}
  .main-nav a{font:bold 12.5px "Arvo",serif;color:var(--white);text-decoration:none;padding:0 10px;border-right:1px dotted rgba(255,255,255,.7)}
  .main-nav a:last-of-type{border-right:0}
  .lang{left:784px;top:60px;width:179px;height:24px;background:#fafafa;border:1px solid #ddd;
    font:9.5px "Questrial",sans-serif;color:#666;display:flex;align-items:center;padding-left:8px}
  .lang i{position:absolute;right:5px;top:4px;width:16px;height:14px;background:var(--lime)}

  .hero-title{left:0;width:1066px;top:312px;text-align:center;font-size:45px;color:var(--ink);letter-spacing:-1px}
  .cta{left:418px;top:370px;width:253px;height:51px;border-radius:5px;
    background:linear-gradient(#d6dc2c,#aab510);box-shadow:0 4px 0 #8f970c;
    display:flex;align-items:center;justify-content:center;gap:12px;
    font-size:27px;color:var(--white);letter-spacing:-.5px}

  .card{top:472px;width:164px;height:205px;background:linear-gradient(#fdfdfd,#e9e9e9);border:1px solid #e2e2e2;
    box-shadow:0 8px 8px -6px rgba(0,0,0,.15)}
  .card svg.tab{position:absolute;left:4px;top:-1px}
  .card h3{position:absolute;left:0;top:14px;width:100%;text-align:center;font:500 27px "Yanone Kaffeesatz",sans-serif;color:var(--white)}
  .card .rule{position:absolute;left:18px;right:18px;top:91px;border-top:1px dotted #bbb}
  .card p{position:absolute;left:18px;right:14px;top:106px;font-size:9.6px;line-height:12.4px;color:var(--muted)}
  .card .corner{position:absolute;right:0;bottom:0}

  .welcome-title{left:120px;top:706px;font-size:53px;letter-spacing:-4px;color:var(--lime)}
  .welcome-divider{left:354px;top:713px;height:50px;border-left:1px dotted #bbb}
  .welcome-text{left:371px;top:714px;width:604px;font-size:11.3px;line-height:13.5px;color:var(--text)}
  .readmore{font-size:11.5px;color:#555;font-weight:bold;letter-spacing:-.3px}
  .line-dotted{left:201px;top:782px;width:735px;border-top:1px dotted #ccc}

  .panel{left:0;top:816px;width:1095px;height:242px;background:var(--panel)}
  .panel h2{position:absolute;font:400 21px "Yanone Kaffeesatz",sans-serif;color:var(--orange);letter-spacing:-.2px}
  .col-divider{top:842px;height:175px;border-left:1px dotted #aaa}
  .news h4{font-weight:normal;font-size:12.3px;color:#666}
  .news p{font-size:9.8px;line-height:12.5px;color:var(--muted);margin-top:3px}
  .partner{left:415px;top:876px;width:233px;height:140px;display:flex;align-items:center;justify-content:center;
    flex-direction:column;border-left:1px solid #dcdcdc;border-right:1px solid #dcdcdc}
  .partner-name{font-size:26px;color:#8e8e8e}
  .field{left:716px;width:242px;height:22px;background:var(--white);border:1px solid #ccc;font-size:9px;color:#777;
    display:flex;align-items:center;padding-left:6px}
  .signup{left:906px;top:935px;width:52px;height:21px;background:var(--orange);font-size:10px;font-weight:bold;color:#3b3a4f;
    display:flex;align-items:center;justify-content:center}

  .accent{left:0;top:1098px;width:1095px;height:7px;background:var(--lime)}
  .footer{left:0;top:1105px;width:1095px;height:95px;background:var(--footer)}
  .footer-nav{left:120px;top:1131px;display:flex;gap:16px}
  .footer-nav a{font:bold 12px "Arvo",serif;color:var(--white);text-decoration:none}
  .copy{left:121px;top:1160px;font-size:11px;color:#e6e6e6}
  .footer-brand{left:880px;top:1120px;display:flex;align-items:center;gap:6px}
  .footer-brand span{width:62px;height:62px;border-radius:50%;background:#77767e;display:block}
  .footer-brand b{font-weight:normal;font-size:24px;color:#d2d2d2}
</style>
</head>
<body>

<div class="abs hero-art" role="img" aria-label="City skyline with silhouettes of businesswomen standing on a light ray-patterned ground"></div>

<div class="abs brand"><span class="brand-disc"></span><span class="brand-name">PVX</span></div>

<form class="login">
  <input class="abs" style="left:481px;top:19px;width:137px" value="Username" aria-label="Username">
  <input class="abs" style="left:624px;top:19px;width:137px" value="Password" aria-label="Password">
</form>
<div class="abs login-btn">LOGIN</div>
<div class="abs social" style="left:858px;top:17px" aria-label="Social links"><span></span><span></span><span></span><span></span></div>

<nav class="abs main-nav">
  <a href="#">Accueil</a><a href="#">Procuvantix</a><a href="#">Metiers</a><a href="#">Nos Refferences</a><a href="#">Contact</a>
</nav>
<div class="abs lang">SELECT LANGUAGE<i></i></div>

<h1 class="abs hero-title">PVX ACTIVITIES</h1>
<div class="abs cta">FREE PROPOSAL
  <svg width="16" height="18" viewBox="0 0 16 18"><path d="M0 0 L16 9 L0 18Z" fill="#fff"/></svg>
</div>

<!-- activity cards -->
<div class="abs card" style="left:120px">
  <svg class="tab" width="156" height="75"><path d="M0 0H156L144 74H12Z" fill="var(--orange)"/></svg>
  <h3>Communaute</h3><div class="rule"></div>
  <p>Lorem ipsum dolor sit amet, consectetur adipiscing elit. Duis commodo Lorem ips um dolor sit amet, consec tetur adipiscing elit. Duis com modo...</p>
  <svg class="corner" width="22" height="22"><path d="M22 0V22H0Z" fill="#555"/><path d="M13 14l4 2.5-4 2.5z" fill="#fff"/></svg>
</div>
<div class="abs card" style="left:292px">
  <svg class="tab" width="156" height="75"><path d="M0 0H156L144 74H12Z" fill="var(--lime)"/></svg>
  <h3>Consulting</h3><div class="rule"></div>
  <p>Lorem ipsum dolor sit amet, consectetur adipiscing elit. Duis commodo Lorem ips um dolor sit amet, consec tetur adipiscing elit. Duis com modo...</p>
  <svg class="corner" width="22" height="22"><path d="M22 0V22H0Z" fill="#555"/><path d="M13 14l4 2.5-4 2.5z" fill="#fff"/></svg>
</div>
<div class="abs card" style="left:464px">
  <svg class="tab" width="156" height="75"><path d="M0 0H156L144 74H12Z" fill="var(--orange)"/></svg>
  <h3>Formation</h3><div class="rule"></div>
  <p>Lorem ipsum dolor sit amet, consectetur adipiscing elit. Duis commodo Lorem ips um dolor sit amet, consec tetur adipiscing elit. Duis com modo...</p>
  <svg class="corner" width="22" height="22"><path d="M22 0V22H0Z" fill="#555"/><path d="M13 14l4 2.5-4 2.5z" fill="#fff"/></svg>
</div>
<div class="abs card" style="left:637px">
  <svg class="tab" width="156" height="75"><path d="M0 0H156L144 74H12Z" fill="var(--lime)"/></svg>
  <h3>TrusoMark</h3><div class="rule"></div>
  <p>Lorem ipsum dolor sit amet, consectetur adipiscing elit. Duis commodo Lorem ips um dolor sit amet, consec tetur adipiscing elit. Duis com modo...</p>
  <svg class="corner" width="22" height="22"><path d="M22 0V22H0Z" fill="#555"/><path d="M13 14l4 2.5-4 2.5z" fill="#fff"/></svg>
</div>
<div class="abs card" style="left:810px">
  <svg class="tab" width="156" height="75"><path d="M0 0H156L144 74H12Z" fill="var(--orange)"/></svg>
  <h3>Multi-Devis</h3><div class="rule"></div>
  <p>Lorem ipsum dolor sit amet, consectetur adipiscing elit. Duis commodo Lorem ips um dolor sit amet, consec tetur adipiscing elit. Duis com modo...</p>
  <svg class="corner" width="22" height="22"><path d="M22 0V22H0Z" fill="#555"/><path d="M13 14l4 2.5-4 2.5z" fill="#fff"/></svg>
</div>

<h2 class="abs welcome-title">WELCOME</h2>
<div class="abs welcome-divider"></div>
<div class="abs welcome-text">
  Maecenas tristique, enim nec lobortis posuere, turpis risus congue lectus, vitae cursus tellus mi vel urna. Pellentesque nec metus ac neque sagittis semper in sed magna. Etiam scelerisque ornare ullamcorper. Praesent sagittis volutpat ipsum, id luctus mauris bibendum eu. Nulla interdum vestibulum arcu luctus facilisis. Phasellus vehicula...
  <div class="readmore" style="text-align:right;margin-top:4px">Readmore...</div>
</div>
<div class="abs line-dotted"></div>

<section class="abs panel"></section>
<h2 class="abs" style="left:120px;top:840px;font:400 21px 'Yanone Kaffeesatz',sans-serif;color:var(--orange)">NEWS ARTICLES</h2>
<h2 class="abs" style="left:409px;top:840px;font:400 21px 'Yanone Kaffeesatz',sans-serif;color:var(--orange)">PARTNERS</h2>
<h2 class="abs" style="left:712px;top:840px;font:400 21px 'Yanone Kaffeesatz',sans-serif;color:var(--orange)">SIGN UP FOR NEWSLETTER</h2>
<div class="abs col-divider" style="left:379px"></div>
<div class="abs col-divider" style="left:683px"></div>

<div class="abs news" style="left:120px;top:876px;width:235px">
  <h4>Lorem Ipsum dolor sit amet....</h4>
  <p>Lorem ipsum dolor sit amet, consectetur adipisc ing elit. Duis commodo...</p>
  <div style="border-top:1px dotted #bbb;margin:12px 26px 10px"></div>
  <h4>Lorem Ipsum dolor sit amet....</h4>
  <p>Lorem ipsum dolor sit amet, consectetur adipisc ing elit. Duis commodo...</p>
  <div class="readmore" style="text-align:right;margin-top:14px;padding-right:8px">Readmore...</div>
</div>

<div class="abs partner"><span class="partner-name">Kestrel Allies</span></div>

<div class="abs field" style="top:876px">Name...</div>
<div class="abs field" style="top:906px">Enter Email Address ...</div>
<div class="abs signup">SIGNUP</div>
<h2 class="abs" style="left:720px;top:979px;font:400 21px 'Yanone Kaffeesatz',sans-serif;color:var(--orange)">FOLLOW US</h2>
<div class="abs social" style="left:836px;top:979px"><span></span><span></span><span></span><span></span></div>

<div class="abs accent"></div>
<footer class="abs footer"></footer>
<nav class="abs footer-nav">
  <a href="#">Accueil</a><a href="#">Procuvantix</a><a href="#">Metiers</a><a href="#">Nos Refferences</a><a href="#">Contact</a>
</nav>
<div class="abs copy">2013 PVX, All Rights Reserved. &nbsp; Privacy Policy - Terms of Conditions.</div>
<div class="abs footer-brand"><span></span><b>PVX</b></div>

</body>
</html>
```